App Design for FlavorRoam

We need an app design for a new app called FlavorRoam, which is an app designed to inspire exploration through personalized recipe generation, local restaurant discoveries, and a vibrant community platform. It caters to food enthusiasts looking to explore global cuisines or find the best local dining spots, offering a premium experience with selected features available for free.

-------UPDATED-----
This app will be AI Driven and may not be heavily dependent on media (images,videos) at first, especially for the Recipe generator feature. Our goal is to still have attractive UI. The core functionalities we are looking are the following
1. Recipe Generator: Either user choose a specific cuisine(italian,spanish), or user inputs ingredients and get recipe, or get recipe for different occasions (xmas, thanksgiving ) and get a randomly get recipe to cook, plain simple. We expect the recipes to be displayed in clear and not too generic manner starting with ingredients and expected duration at top and then step by step guide. We also intend to enable premium users to have playful action button or icon to get unlimited recipes generated until they find what they like and also have save for later feature. These premium features should be disabled for free users and prompted to subscribe if they click them with nice popup
2. Restaurant Recommendation - will have selected pictures and will be based on inputs such as zip code and other filters such as cousine types. Premium users can filter by price range, get unlimited recommendation, see actual price range in the recommendation and can save for later where they can find it later. Free users cannot filter by price (disabled) and should see it hidden in the recommendation
3. Meal Planning - will include just simple and random meal plan with just one button or limited interaction for free, users need to subscribe to get features such as customized plan such as considering allergies or diet preferences. Premium users can also get a shopping checklist of ingredients for weekly meal preps and their step by step guide for each meal recipe.
2. Community Sharing: users can view posts and engage with community content
Updates

Hello Designers,

The initial price was not fair for the work. So I have increased it. There will also be $50-100 bonus for those who come up with great designs or for those who incorporate interesting stuff. Thank you! Much appreciated 🙏

Colors
0054AA
0677BA
7BADD7
CADEEF
E8F1F8
0094D4
00A9DD
6FCCEA
C7EBF8
E9F6FB
00AB8E
00BBA5
67D7C9
C6EFE9
E9F9F6
FFC000
F8CF3A
FAE287
FDF2CF
FEFAEE
F0912C
F2A743
F7CA91
FBE8D2
FDF5EE
EE7325
F08F49
F5BC92
FAE3D3
FDF4ED
A7469A
B969AE
D3A5CF
EDDBEB
F8F0F9
6B429C
8869AF
B7A5CE
E3DAEB
F3F0F8

```html
<!DOCTYPE html>
<html lang="en">
<head>
<meta charset="utf-8">
<title>FlavorRoam – App Screens</title>
<link href="https://fonts.googleapis.com/css2?family=Plus+Jakarta+Sans:wght@400;500;600;700;800&display=swap" rel="stylesheet">
<style>
  :root{
    --bg:#3a2a14;
    --orange:#EE7325;
    --orange-2:#F0912C;
    --amber:#F8A21A;
    --red-x:#e8413b;
    --ink:#1b1b1b;
    --muted:#8a8a8a;
    --line:#e6e6e6;
    --white:#ffffff;
    --label:#b9a98e;
  }
  *{box-sizing:border-box;margin:0;padding:0}
  html,body{width:771px;height:1200px;overflow:hidden;background:var(--bg)}
  body{font-family:"Plus Jakarta Sans",sans-serif;color:var(--ink);position:relative}
  .screen-label{position:absolute;font-size:9px;letter-spacing:4px;color:var(--label);font-weight:500;
    transform:rotate(-90deg);transform-origin:left top;white-space:nowrap}
  .screen{position:absolute;width:210px;background:var(--white);border-radius:26px;overflow:hidden;
    box-shadow:0 0 0 5px #111}
  .status{position:absolute;top:12px;left:0;right:0;display:flex;justify-content:space-between;padding:0 20px 0 26px;font-size:8.5px;font-weight:600}
  .status .icons{display:flex;gap:3px;align-items:center}
  .status .bars{width:9px;height:6px;background:currentColor;clip-path:polygon(0 100%,100% 0,100% 100%)}
  .status .wifi{width:8px;height:6px;background:currentColor;border-radius:8px 8px 0 0;clip-path:polygon(50% 100%,0 0,100% 0)}
  .status .battery{width:12px;height:6px;background:currentColor;border-radius:1.5px}
  .home-bar{position:absolute;left:68px;width:74px;height:2.5px;border-radius:2px;background:#111}
  .arrow-btn{position:absolute;width:17px;height:17px;border-radius:50%;background:var(--amber);display:flex;align-items:center;justify-content:center}
  .art-ring{position:absolute;border-radius:50%;background:#fff;box-shadow:0 3px 8px rgba(0,0,0,.15);padding:4px}
  .art-ring .art{width:100%;height:100%;border-radius:50%}
  /* main screen */
  .avatar{position:absolute;left:14px;top:40px;width:26px;height:26px;border-radius:50%;background:linear-gradient(135deg,#5a7ea3,#9c8060)}
  .menu-btn{position:absolute;right:14px;top:42px;width:22px;height:22px;border-radius:50%;background:#fff;box-shadow:0 1px 5px rgba(0,0,0,.15);display:flex;align-items:center;justify-content:center}
  .greet{position:absolute;left:14px;top:80px;font-size:7px;font-weight:600}
  .headline{position:absolute;left:14px;top:91px;font-size:14.5px;font-weight:800;letter-spacing:-.2px}
  .choice{position:absolute;font-size:8.5px;font-weight:600}
  /* recipe screens */
  .header-title{position:absolute;top:43px;left:0;right:0;text-align:center;color:#fff;font-size:10px;font-weight:700}
  .back-btn{position:absolute;left:13px;top:40px;width:21px;height:21px;border-radius:50%;background:#fff;display:flex;align-items:center;justify-content:center}
  .section-title{position:absolute;left:13px;font-size:8.5px;font-weight:700}
  .tiles{position:absolute;left:13px;right:13px;top:181px;height:41px;display:flex;gap:6px}
  .tile{flex:1;border:1px solid var(--line);border-radius:5px;display:flex;flex-direction:column;align-items:center;justify-content:center;gap:5px;font-size:5px;color:#555}
  .tile.active{border-color:var(--orange-2);color:var(--orange);font-weight:700}
  .ingredients{position:absolute;left:13px;right:13px;top:272px;border-left:2px solid var(--line);padding-left:8px}
  .ingredient{height:21.5px;display:flex;justify-content:space-between;align-items:center;font-size:7px}
  .ingredient .remove{color:var(--red-x);font-size:9px;line-height:1}
  .add-ingredient{color:#aaa;gap:5px;justify-content:flex-start}
  .add-ingredient .plus{width:9px;height:9px;border-radius:50%;background:var(--amber);color:#fff;font-size:8px;display:flex;align-items:center;justify-content:center;font-weight:700}
  .chips{position:absolute;left:13px;right:13px;top:423px;height:20px;display:flex;gap:6px}
  .chip{flex:1;border:1px solid var(--line);border-radius:5px;display:flex;align-items:center;justify-content:center;font-size:7px}
  .chip.active{border-color:var(--orange-2);color:var(--orange);font-weight:700}
  .chips.disabled .chip{color:#cfcfcf;border-color:#f0f0f0}
  .cta{position:absolute;left:13px;right:13px;top:474px;height:25px;border-radius:13px;background:linear-gradient(90deg,var(--orange-2),var(--amber));color:#fff;font-size:7.5px;font-weight:700;display:flex;align-items:center;justify-content:center;gap:6px;box-shadow:0 3px 8px rgba(240,145,44,.35)}
  .cta .pen{width:11px;height:11px;border-radius:50%;background:#fff}
  .subscribe-zone{position:absolute;left:0;right:0;top:522px;height:76px;background:#fafafa}
  .alarm{position:absolute;left:89px;top:-10px;width:32px;height:32px;border-radius:50%;background:#fff;box-shadow:0 2px 6px rgba(0,0,0,.1);display:flex;align-items:center;justify-content:center}
  .subscribe-text{position:absolute;top:47px;left:0;right:0;text-align:center;font-size:6px;font-weight:700;color:var(--orange)}
</style>
</head>
<body>

<!-- Main screen -->
<div class="screen-label" style="left:34px;top:690px">MAIN SCREEN</div>
<section class="screen main-screen" style="left:58px;top:300px;height:458px">
  <svg width="210" height="458" style="position:absolute;left:0;top:0" aria-hidden="true">
    <defs><linearGradient id="blob" x1="0" y1="0" x2="0" y2="1"><stop offset="0" stop-color="#F7A12A"/><stop offset="1" stop-color="#EE6A25"/></linearGradient></defs>
    <path d="M0 126 Q60 110 80 150 Q110 215 85 290 Q60 370 0 420 Z" fill="url(#blob)"/>
  </svg>
  <div class="status"><span>9:41</span><span class="icons"><i class="bars"></i><i class="wifi"></i><i class="battery"></i></span></div>
  <div class="avatar" role="img" aria-label="User profile photo"></div>
  <div class="menu-btn"><svg width="9" height="7"><path d="M0 1h9M0 3.5h9M0 6h9" stroke="#F0912C" stroke-width="1.2"/></svg></div>
  <div class="greet">Hi Marco,</div>
  <h1 class="headline">What’d you like today?</h1>

  <div class="art-ring" style="left:17px;top:131px;width:68px;height:68px"><div class="art" role="img" aria-label="Illustration of a clay pot with palm leaves" style="background:radial-gradient(circle,#b07a3a,#6f9a3a 70%,#f3efe6 72%)"></div></div>
  <div class="choice" style="left:96px;top:160px">Get a recipe</div>
  <div class="arrow-btn" style="left:157px;top:157px"><svg width="8" height="8"><path d="M1 4h6M4.5 1.5 7 4 4.5 6.5" stroke="#fff" stroke-width="1.2" fill="none"/></svg></div>

  <div class="art-ring" style="left:51px;top:234px;width:68px;height:68px"><div class="art" role="img" aria-label="Illustration of a restaurant menu with cutlery" style="background:radial-gradient(circle,#f6b21c,#e8452b 70%,#f3efe6 72%)"></div></div>
  <div class="choice" style="left:129px;top:263px">Eat out</div>
  <div class="arrow-btn" style="left:168px;top:260px"><svg width="8" height="8"><path d="M1 4h6M4.5 1.5 7 4 4.5 6.5" stroke="#fff" stroke-width="1.2" fill="none"/></svg></div>

  <div class="art-ring" style="left:17px;top:336px;width:68px;height:68px"><div class="art" role="img" aria-label="Illustration of a calendar and cooking pot" style="background:radial-gradient(circle,#7bb0e8,#3a6ad6 70%,#f3efe6 72%)"></div></div>
  <div class="choice" style="left:96px;top:365px">Plan a meal</div>
  <div class="arrow-btn" style="left:156px;top:362px"><svg width="8" height="8"><path d="M1 4h6M4.5 1.5 7 4 4.5 6.5" stroke="#fff" stroke-width="1.2" fill="none"/></svg></div>

  <div class="home-bar" style="top:447px"></div>
</section>

<!-- Recipe screen, subscribed -->
<div class="screen-label" style="left:272px;top:830px">GET A RECIPE SCREEN - SUBSCRIBED</div>
<section class="screen recipe-screen" style="left:294px;top:300px;height:522px">
  <svg width="210" height="130" style="position:absolute;left:0;top:0" aria-hidden="true">
    <defs><linearGradient id="hdr" x1="0" y1="0" x2="0" y2="1"><stop offset="0" stop-color="#F0912C"/><stop offset="1" stop-color="#EE6A25"/></linearGradient></defs>
    <path d="M0 0H210V74Q105 136 0 74Z" fill="url(#hdr)"/>
  </svg>
  <div class="status" style="color:#fff"><span>9:41</span><span class="icons"><i class="bars"></i><i class="wifi"></i><i class="battery"></i></span></div>
  <div class="back-btn"><svg width="9" height="9"><path d="M8 4.5H1.5M4 2 1.5 4.5 4 7" stroke="#EE7325" stroke-width="1.2" fill="none"/></svg></div>
  <div class="header-title">Get a recipe</div>
  <div class="art-ring" style="left:70px;top:72px;width:70px;height:70px"><div class="art" role="img" aria-label="Illustration of a clay pot with palm leaves" style="background:radial-gradient(circle,#b07a3a,#6f9a3a 70%,#f3efe6 72%)"></div></div>

  <div class="section-title" style="top:161px">Customize your recipe</div>
  <div class="tiles">
    <div class="tile active"><svg width="12" height="12"><path d="M3 9 10 2" stroke="#EE7325" stroke-width="2.5"/></svg>Add Ingredients</div>
    <div class="tile"><svg width="12" height="10"><path d="M1 9h10M2 8a4 4 0 0 1 8 0Z" fill="#c9c9c9" stroke="#c9c9c9"/></svg>Cuisine</div>
    <div class="tile"><svg width="12" height="10"><rect x="1" y="4" width="10" height="6" fill="#c9c9c9"/><rect x="5.5" y="0" width="1" height="4" fill="#c9c9c9"/></svg>Occasion</div>
  </div>

  <div class="section-title" style="top:248px">Add your ingredients</div>
  <div class="ingredients">
    <div class="ingredient"><span>Beef</span><span class="remove">×</span></div>
    <div class="ingredient"><span>Onions</span><span class="remove">×</span></div>
    <div class="ingredient"><span>Tomatoes</span><span class="remove">×</span></div>
    <div class="ingredient"><span>Capsicum</span><span class="remove">×</span></div>
    <div class="ingredient add-ingredient"><span class="plus">+</span><span>add ingredient</span></div>
  </div>

  <div class="section-title" style="top:401px">Maximum Cooking Time</div>
  <div class="chips">
    <div class="chip">30 mins</div>
    <div class="chip active">1 hr</div>
    <div class="chip">2 hrs</div>
  </div>
  <div class="cta"><span class="pen"></span>Get your recipe</div>
  <div class="home-bar" style="top:512px"></div>
</section>

<!-- Recipe screen, not subscribed -->
<div class="screen-label" style="left:512px;top:866px">GET A RECIPE SCREEN - NOT SUBSCRIBED</div>
<section class="screen recipe-screen" style="left:534px;top:300px;height:598px">
  <svg width="210" height="130" style="position:absolute;left:0;top:0" aria-hidden="true">
    <path d="M0 0H210V74Q105 136 0 74Z" fill="url(#hdr)"/>
  </svg>
  <div class="status" style="color:#fff"><span>9:41</span><span class="icons"><i class="bars"></i><i class="wifi"></i><i class="battery"></i></span></div>
  <div class="back-btn"><svg width="9" height="9"><path d="M8 4.5H1.5M4 2 1.5 4.5 4 7" stroke="#EE7325" stroke-width="1.2" fill="none"/></svg></div>
  <div class="header-title">Get a recipe</div>
  <div class="art-ring" style="left:70px;top:72px;width:70px;height:70px"><div class="art" role="img" aria-label="Illustration of a clay pot with palm leaves" style="background:radial-gradient(circle,#b07a3a,#6f9a3a 70%,#f3efe6 72%)"></div></div>

  <div class="section-title" style="top:161px">Customize your recipe</div>
  <div class="tiles">
    <div class="tile active"><svg width="12" height="12"><path d="M3 9 10 2" stroke="#EE7325" stroke-width="2.5"/></svg>Add Ingredients</div>
    <div class="tile"><svg width="12" height="10"><path d="M1 9h10M2 8a4 4 0 0 1 8 0Z" fill="#c9c9c9" stroke="#c9c9c9"/></svg>Cuisine</div>
    <div class="tile"><svg width="12" height="10"><rect x="1" y="4" width="10" height="6" fill="#c9c9c9"/><rect x="5.5" y="0" width="1" height="4" fill="#c9c9c9"/></svg>Occasion</div>
  </div>

  <div class="section-title" style="top:248px">Add your ingredients</div>
  <div class="ingredients">
    <div class="ingredient"><span>Beef</span><span class="remove">×</span></div>
    <div class="ingredient"><span>Onions</span><span class="remove">×</span></div>
    <div class="ingredient"><span>Tomatoes</span><span class="remove">×</span></div>
    <div class="ingredient"><span>Capsicum</span><span class="remove">×</span></div>
    <div class="ingredient add-ingredient"><span class="plus">+</span><span>add ingredient</span></div>
  </div>

  <div class="section-title" style="top:401px">Maximum Cooking Time</div>
  <div class="chips disabled">
    <div class="chip">30 mins</div>
    <div class="chip">1 hr</div>
    <div class="chip">2 hrs</div>
  </div>
  <div class="cta"><span class="pen"></span>Get your recipe</div>

  <div class="subscribe-zone">
    <div class="alarm"><svg width="14" height="14"><circle cx="7" cy="8" r="5" fill="#EE7325"/><path d="M7 5.5V8h2" stroke="#fff" stroke-width="1.2" fill="none"/></svg></div>
    <div class="subscribe-text">Subscribe to add maximum cooking time</div>
  </div>
  <div class="home-bar" style="top:588px"></div>
</section>

</body>
</html>
```